qLM Builders
Nimble Site Crafting
draft #229 - This looks pretty good. We prefer option 2 for the stationary. Clean and simple. We aren't so sure about the colored watermark. Seems like too much maybe
draft #223 - We really like the back of this one!
The contests has been extended for 3 more days. Please submit new designs. Due to the short time frame, we will only be accepting and rating full designs including complete stationary.
I will make every effort to provide feedback as soon as possible on designs concepts. Thank!
draft #96 - I like the back! The front is a little cookie cutter. Can you try something that integrates the "X" into the design. I don't really like the text all centered (draft #95,draft #94)
draft #102 I don't like the graphic at the top, but I like the back and I like how you integrated the X on the front like a watermark. can you remove that and add some icon's for phone,email, ect?
Some design inspiration - here are some cards we like
http://www.cardmarket.example/theme_previews/1778907-stylish-business-card?index=4
http://cardmarket.example/item/royal-modern-business-card/2484567?WT.ac=category_thumb&WT.seg_1=category_thumb&WT.z_author=omar-lindqvest
http://cardmarket.example/item/awesomeness-business-card/55256?WT.ac=category_thumb&WT.seg_1=category_thumb&WT.z_author=Bram
http://cardmarket.example/item/qr-business-card/1361513?WT.ac=category_thumb&WT.seg_1=category_thumb&WT.z_author=Marisk
http://cardmarket.example/item/clean-modern-business-card/1922436?WT.ac=category_thumb&WT.seg_1=category_thumb&WT.z_author=dustwick
http://cardmarket.example/theme_previews/1492534-neat-corporate-business-card?index=9
http://cardmarket.example/item/red-business-card/504464?WT.ac=category_thumb&WT.seg_1=category_thumb&WT.z_author=lumenpress
Also meant to mention, we prefer square cards (instead of the rounded corners).
If you have ideas for texture/embossing that would look nice please include! We are digging the glossy look on the back of some of these. But any details that help make the card unique is great!
thanks again!
Hi Designers. We got backed up and haven't been able to provide feedback yet.
There are also A LOT of designs to go through. We will be eliminating design's I consider "cookie cutter" templates. We are interested in unique designs that integrate the with the look and feel of the logo, or directly integrate parts of the logo with the designs.
In General, the Wavy/curvy look isn't what we are going for (there are A LOT of those).
There are some very unique integrations with the "X" that we like, especially when it's used kinda like a watermark.
We don't want any contact info on the back other then maybe the website.
Again thanks for your work! We will be sending specific feedback for the designs we like via PM in the next few hours.
Gavin@qlmbuilders
Thanks for all the designs and the note. We will be going through and selecting the few our favorite designs so far and offering tomorrow.
Thanks for the good work!
@PH - we will develop stationery for the liked business cards. Please let me know via private message. Thanks
sir please check pvt message top right side please
Note to Designers - This a a business Card & Stationary project. Designs should include concepts for both. Any questions or concerns please message me.

```html
<!DOCTYPE html>
<html lang="en">
<head>
<meta charset="utf-8">
<title>qLM Builders – Business Cards</title>
<link rel="stylesheet" href="https://fonts.googleapis.com/css2?family=Exo+2:wght@400;600&family=Open+Sans:wght@400;600;700&display=swap">
<style>
  :root {
    --bg: #2b2c2e;
    --brand-blue: #2fa8dc;
    --brand-blue-light: #6fd0f4;
    --brand-blue-deep: #1b8cc4;
    --card-white: #ffffff;
    --ink-dark: #3a3d40;
    --ink-grey: #6c7074;
    --icon-blue: #38a7d8;
  }
  * { margin: 0; padding: 0; box-sizing: border-box; }
  html, body {
    width: 1200px; height: 901px; overflow: hidden;
    background: var(--bg);
  }
  .stage {
    position: relative; width: 1200px; height: 901px;
  }
  .card {
    position: absolute;
    width: 520px; height: 297px;
    top: 302px;
    box-shadow: 0 14px 34px rgba(0,0,0,0.45);
    overflow: hidden;
  }

  /* Back of card */
  .card-back {
    left: 50px;
    background: linear-gradient(135deg, var(--brand-blue-light) 0%, var(--brand-blue) 55%, var(--brand-blue-deep) 100%);
  }
  .card-back .back-sheen {
    position: absolute; inset: 0;
    background: linear-gradient(160deg, rgba(255,255,255,0.28) 0%, rgba(255,255,255,0) 45%);
  }
  .card-back .back-brand {
    position: absolute; right: 36px; top: 104px;
    text-align: right; color: var(--card-white);
  }
  .back-brand .brand-name {
    font-family: "Exo 2", sans-serif; font-weight: 600;
    font-size: 34px; letter-spacing: 1px; line-height: 1;
  }
  .back-brand .brand-tagline {
    font-family: "Open Sans", sans-serif; font-weight: 600;
    font-size: 15px; letter-spacing: 0.5px; margin-top: 6px;
  }
  .back-brand .brand-web {
    font-family: "Open Sans", sans-serif; font-weight: 600;
    font-size: 13px; letter-spacing: 1.2px; margin-top: 6px;
  }

  /* Front of card */
  .card-front {
    left: 630px;
    background: var(--card-white);
  }
  .edge-tab {
    position: absolute; background: var(--brand-blue); width: 8px;
  }
  .edge-tab.right { right: 0; top: 38px; height: 96px; }
  .edge-tab.left { left: 0; top: 210px; height: 66px; }

  .front-brand {
    position: absolute; left: 40px; top: 42px;
    display: flex; align-items: center; gap: 12px;
  }
  .front-brand .brand-square {
    width: 34px; height: 34px; background: var(--brand-blue);
  }
  .front-brand .brand-name {
    font-family: "Exo 2", sans-serif; font-weight: 600;
    font-size: 30px; color: var(--brand-blue); letter-spacing: 1px; line-height: 1;
  }
  .front-tagline {
    position: absolute; left: 86px; top: 78px;
    font-family: "Open Sans", sans-serif; font-weight: 700;
    font-size: 13px; color: var(--ink-dark); letter-spacing: 0.6px;
  }

  .person {
    position: absolute; right: 40px; top: 110px; text-align: right;
    font-family: "Open Sans", sans-serif;
  }
  .person .person-name { font-weight: 700; font-size: 15px; color: var(--brand-blue); }
  .person .person-role { font-size: 12px; color: var(--ink-grey); margin-top: 2px; }

  .address {
    position: absolute; left: 40px; top: 166px;
    font-family: "Open Sans", sans-serif; font-weight: 600;
    font-size: 12px; line-height: 1.35; color: var(--ink-dark);
  }
  .contact-list {
    position: absolute; left: 40px; top: 214px; list-style: none;
    font-family: "Open Sans", sans-serif; font-weight: 600;
    font-size: 12px; color: var(--ink-dark);
  }
  .contact-list li { display: flex; align-items: center; gap: 9px; height: 21px; }
  .contact-icon { width: 13px; height: 13px; flex: none; }
</style>
</head>
<body>
<main class="stage">

  <section class="card card-back" aria-label="Business card back">
    <div class="back-sheen"></div>
    <div class="back-brand">
      <div class="brand-name">qLM Builders</div>
      <div class="brand-tagline">Nimble Site Crafting</div>
      <div class="brand-web">www.qlmbuilders.com</div>
    </div>
  </section>

  <section class="card card-front" aria-label="Business card front">
    <span class="edge-tab right"></span>
    <span class="edge-tab left"></span>

    <div class="front-brand">
      <span class="brand-square"></span>
      <span class="brand-name">qLM Builders</span>
    </div>
    <div class="front-tagline">Nimble Site Crafting</div>

    <div class="person">
      <div class="person-name">Gavin Holloway</div>
      <div class="person-role">Owner, CEO</div>
    </div>

    <div class="address">218 Orbit Lane<br>Lakeview, WI 53790</div>

    <ul class="contact-list">
      <li>
        <svg class="contact-icon" viewBox="0 0 16 16" aria-hidden="true">
          <circle cx="8" cy="8" r="8" fill="var(--icon-blue)"/>
          <path d="M5.2 4.2l1.6 1.6-.9 1.1c.5 1 1.2 1.7 2.2 2.2l1.1-.9 1.6 1.6-.9 1.4c-2.9-.4-5.1-2.6-5.5-5.5z" fill="#fff"/>
        </svg>
        <span>6085550142</span>
      </li>
      <li>
        <svg class="contact-icon" viewBox="0 0 16 16" aria-hidden="true">
          <circle cx="8" cy="8" r="8" fill="var(--icon-blue)"/>
          <rect x="4" y="5.2" width="8" height="5.6" fill="#fff"/>
          <path d="M4 5.4l4 3 4-3" fill="none" stroke="var(--icon-blue)" stroke-width="0.9"/>
        </svg>
        <span>gavin@qlmbuilders.com</span>
      </li>
      <li>
        <svg class="contact-icon" viewBox="0 0 16 16" aria-hidden="true">
          <circle cx="8" cy="8" r="8" fill="var(--icon-blue)"/>
          <circle cx="8" cy="8" r="3.8" fill="none" stroke="#fff" stroke-width="1"/>
          <path d="M4.2 8h7.6M8 4.2c-1.6 2.2-1.6 5.4 0 7.6M8 4.2c1.6 2.2 1.6 5.4 0 7.6" fill="none" stroke="#fff" stroke-width="0.8"/>
        </svg>
        <span>www.qlmbuilders.com</span>
      </li>
    </ul>
  </section>

</main>
</body>
</html>
```